R&T Builders and Spaces Business Card

We need to redesign our business card. We had used white vellum wih grey logo and txt in the past. I would like to bring a little life into our cards without being over the top. I think I will be going away from the vellum and printing soft touch business cards.
I have attached what we currently have and our new logo design.

```html
<!DOCTYPE html>
<html lang="en">
<head>
<meta charset="utf-8">
<title>R&amp;T Builders and Spaces – Business Card</title>
<link href="https://fonts.googleapis.com/css2?family=Jost:wght@300;400;600;700&display=swap" rel="stylesheet">
<style>
  :root {
    --backdrop: #737373;
    --card-front: #111111;
    --card-back: #c0c0c0;
    --white: #ffffff;
    --mark-grey: #5a5a5a;
    --name-grey: #9a9a9a;
    --logo-text: #c0c0c0;
  }
  * { margin: 0; padding: 0; box-sizing: border-box; }
  html, body {
    width: 1200px; height: 1200px; overflow: hidden;
    background: var(--backdrop);
    font-family: "Jost", "Futura", sans-serif;
  }
  .canvas { position: relative; width: 1200px; height: 1200px; }

  .card { position: absolute; width: 746px; height: 436px; }
  .card--front {
    left: 226px; top: 139px;
    background: var(--card-front);
    box-shadow: 0 14px 40px rgba(0,0,0,0.35);
    display: flex; align-items: center; justify-content: center;
  }
  .card--back {
    left: 222px; top: 637px;
    background: var(--card-back);
  }

  .brand { display: flex; align-items: center; gap: 18px; }
  .brand__square { width: 40px; height: 40px; background: var(--mark-grey); }
  .brand__name {
    color: var(--name-grey); font-weight: 400; font-size: 30px;
    letter-spacing: 0.06em; text-transform: uppercase;
  }

  .brand-block {
    position: absolute; left: 80px; top: 111px;
    width: 219px; height: 219px; background: var(--white);
    display: flex; align-items: center; justify-content: center;
    text-align: center; padding: 20px;
  }
  .brand-block__name {
    color: var(--logo-text); font-weight: 400; font-size: 24px;
    line-height: 1.25; letter-spacing: 0.05em; text-transform: uppercase;
  }

  .contact {
    position: absolute; left: 392px; width: 240px; top: 0;
    color: var(--white); text-align: center;
  }
  .contact__name {
    position: absolute; top: 104px; width: 100%;
    font-weight: 600; font-size: 22px; letter-spacing: 0.12em;
  }
  .contact__title {
    position: absolute; top: 135px; width: 100%;
    font-weight: 400; font-size: 12px; letter-spacing: 0.45em;
  }
  .contact__email {
    position: absolute; top: 166px; width: 100%;
    font-weight: 300; font-size: 25px; letter-spacing: 0.04em;
  }
  .contact__phones {
    position: absolute; top: 211px; left: -20px; width: 280px;
    font-weight: 600; font-size: 16px; letter-spacing: 0.03em;
    display: flex; align-items: center; justify-content: center; gap: 5px;
  }
  .contact__phones svg { width: 12px; height: 14px; fill: var(--white); }
  .contact__web {
    position: absolute; top: 249px; width: 100%;
    font-weight: 300; font-size: 23px;
  }
  .contact__web strong { font-weight: 700; }
  .contact__address {
    position: absolute; top: 291px; width: 100%;
    font-weight: 400; font-size: 13.5px; line-height: 20px;
  }

  .firm-name {
    position: absolute; left: 361px; top: 382px;
    color: var(--white); font-weight: 300; font-size: 31px;
    letter-spacing: 0.12em; white-space: nowrap;
  }
  .firm-tag {
    position: absolute; left: 712px; top: 372px;
    transform-origin: 0 0; transform: rotate(-90deg) translateY(-50%);
    color: var(--white); font-weight: 300; font-size: 31px;
    letter-spacing: 0.12em; white-space: nowrap;
  }
</style>
</head>
<body>
<main class="canvas">
  <section class="card card--front" aria-label="Card front">
    <div class="brand">
      <span class="brand__square"></span>
      <span class="brand__name">R&amp;T Builders and Spaces</span>
    </div>
  </section>

  <section class="card card--back" aria-label="Card back">
    <div class="brand-block">
      <span class="brand-block__name">R&amp;T Builders<br>and Spaces</span>
    </div>

    <div class="contact">
      <p class="contact__name">DANA MARLOWE</p>
      <p class="contact__title">PARTNER</p>
      <p class="contact__email">danam@rtbuilders.com</p>
      <p class="contact__phones">
        <svg viewBox="0 0 12 14" aria-hidden="true"><path d="M2.4 0.6 4.4 3.4 3.2 5c.8 1.7 2 3 3.6 3.9l1.5-1.2 2.9 1.9-1 2.8C6 12.4 1.2 7.5.2 2.2z"/></svg>
        <span>602 555 0148</span>
        <span>|</span>
        <svg viewBox="0 0 12 14" aria-hidden="true"><path d="M2.5 0h7a1 1 0 0 1 1 1v12a1 1 0 0 1-1 1h-7a1 1 0 0 1-1-1V1a1 1 0 0 1 1-1zm.5 2v8.5h6V2zm3 9.3a.9.9 0 1 0 0 1.8.9.9 0 0 0 0-1.8z"/></svg>
        <span>602 555 0172</span>
      </p>
      <p class="contact__web"><strong>rtbuilders</strong>.com</p>
      <p class="contact__address">2400 W. Canyon Rd., Suite 310<br>Tempe, AZ 85281</p>
    </div>

    <p class="firm-name">R&amp;T BUILDERS</p>
    <p class="firm-tag">AND SPACES</p>
  </section>
</main>
</body>
</html>
```